Flyer Design Project

I need a flyer to hand out at events that promotes my web design and web management services
Updates

A5 in size.

Additional Text

Vantaro is single point for all of your online needs.  Affordable web design, development, ecommerce, search engine optimisation, internet marketing and web hosting. 

We offer truly bespoke web design and development services all performed by in-house professionals. Our services are tailored to your needs.

Target Market(s)

small companies/individuals with low budgets

Industry/Entity Type

Events

Requirements
Must have
• vantaro logo
highlighting:
Website Design
Content Management Systems
Ecommerce Websites
Quillpage Blog Design
SEO Services
Social Media Marketing

```html
<!DOCTYPE html>
<html lang="en">
<head>
<meta charset="utf-8">
<title>Vantaro Flyer</title>
<link rel="stylesheet" href="https://fonts.googleapis.com/css2?family=Source+Sans+3:wght@400;700&display=swap">
<style>
  :root {
    --page-bg: #e6e6e6;
    --flyer-dark: #4a4a4a;
    --panel-grey: #5d5d5d;
    --column-grey: #666666;
    --white: #ffffff;
    --text-light: #f2f2f2;
    --blue: #2a66b3;
    --green: #0f9a3a;
    --lime: #c9d400;
    --orange: #de7a12;
    --red: #d63a1f;
    --navy: #1f2459;
    --brand-red: #d8262e;
    --font: "Source Sans 3", Arial, sans-serif;
  }
  html, body {
    margin: 0;
    width: 1200px;
    height: 900px;
    overflow: hidden;
    background: var(--page-bg);
    font-family: var(--font);
  }
  .flyer {
    position: absolute;
    left: 304px;
    top: 30px;
    width: 592px;
    height: 840px;
    background: var(--flyer-dark);
    overflow: hidden;
  }
  .hero {
    position: absolute;
    left: 0; top: 0;
    width: 592px; height: 461px;
    background:
      radial-gradient(ellipse at 45% 40%, rgba(120,200,235,0.55), rgba(120,200,235,0) 55%),
      linear-gradient(160deg, #3c3c3c 0%, #8d8d8d 45%, #cfcfcf 70%, #9a9a9a 100%);
  }
  .hero-rule {
    position: absolute;
    left: 0; top: 461px;
    width: 592px; height: 13px;
    background: var(--white);
  }
  .service-column {
    position: absolute;
    left: 449px; top: 478px;
    width: 116px; height: 218px;
    background: var(--column-grey);
  }
  .services { position: absolute; left: 0; top: 0; width: 592px; height: 840px; }
  .service-label {
    position: absolute;
    height: 23px;
    line-height: 23px;
    padding-left: 10px;
    color: var(--white);
    font-weight: 700;
    font-size: 13px;
    box-sizing: border-box;
    white-space: nowrap;
  }
  .service-label.is-blue { background: var(--blue); }
  .service-label.is-green { background: var(--green); }
  .service-label.is-lime { background: var(--lime); }
  .service-label.is-orange { background: var(--orange); }
  .service-label.is-red { background: var(--red); }
  .service-label.is-navy { background: var(--navy); }
  .about {
    position: absolute;
    left: 24px; top: 717px;
    width: 409px; height: 96px;
    box-sizing: border-box;
    padding: 8px 12px;
    background: var(--panel-grey);
    color: var(--text-light);
    font-size: 11.5px;
    line-height: 1.2;
  }
  .about p { margin: 0 0 8px; }
  .about strong { font-weight: 700; }
  .brand-box {
    position: absolute;
    left: 449px; top: 717px;
    width: 116px; height: 96px;
    background: var(--white);
    display: flex;
    align-items: center;
    justify-content: center;
    gap: 6px;
  }
  .brand-mark {
    width: 14px; height: 14px;
    background: var(--brand-red);
  }
  .brand-name {
    color: var(--brand-red);
    font-weight: 700;
    font-size: 22px;
  }
</style>
</head>
<body>
  <main class="flyer">
    <div class="hero" role="img" aria-label="Photo of a hand touching floating screens showing web and technology images"></div>
    <div class="hero-rule"></div>

    <div class="service-column"></div>

    <svg class="services" width="592" height="840" viewBox="0 0 592 840" aria-hidden="true">
      <g class="service-tabs">
        <polygon points="428,499 449,510 449,533 428,522" fill="#1f4f8c"/>
        <rect x="449" y="510" width="116" height="23" fill="var(--blue)"/>
        <polygon points="428,531 449,542 449,565 428,554" fill="#0b7630"/>
        <rect x="449" y="542" width="116" height="23" fill="var(--green)"/>
        <polygon points="428,564 449,575 449,598 428,587" fill="#9ea600"/>
        <rect x="449" y="575" width="116" height="23" fill="var(--lime)"/>
        <polygon points="428,596 449,607 449,630 428,619" fill="#b0600d"/>
        <rect x="449" y="607" width="116" height="23" fill="var(--orange)"/>
        <polygon points="428,629 449,640 449,663 428,652" fill="#a82c17"/>
        <rect x="449" y="640" width="116" height="23" fill="var(--red)"/>
        <polygon points="428,661 449,672 449,695 428,684" fill="#151940"/>
        <rect x="449" y="672" width="116" height="23" fill="var(--navy)"/>
      </g>
    </svg>

    <div class="service-label is-blue" style="left:17px;top:499px;width:411px;">Website Design</div>
    <div class="service-label is-green" style="left:61px;top:531px;width:367px;">Content Management Systems</div>
    <div class="service-label is-lime" style="left:103px;top:564px;width:325px;">Ecommerce Websites</div>
    <div class="service-label is-orange" style="left:144px;top:596px;width:284px;">Quillpage Blog Design</div>
    <div class="service-label is-red" style="left:185px;top:629px;width:243px;">SEO Services</div>
    <div class="service-label is-navy" style="left:228px;top:661px;width:200px;">Social Media Marketing</div>

    <section class="about">
      <p><strong>Vantaro</strong> is single point for all of your online needs.&nbsp; Affordable web design, development, ecommerce, search engine optimisation, internet marketing and web hosting.</p>
      <p>We offer truly bespoke web design and development services all performed by in-house professionals. Our services are tailored to your needs.</p>
    </section>

    <div class="brand-box">
      <span class="brand-mark"></span>
      <span class="brand-name">vantaro</span>
    </div>
  </main>
</body>
</html>
```